Design a Corporate Brochure

Hi all

We are looking for a design for our corporate brochure.
This brochure is about our company and has to deliver our values and strenghts to our customers.

1. Our slogan: we shelter your business
2. Who is Kalvendor
3. Global presence
4. Our offer: ZEN / MAX range
5. USP's
6. Reference buildings / industry

Attached you will find:
- Corporate brandbrand / style guide: with colors, fonts, logo use, etc..
- example of brochures in right style
- Needed pictures
- Our draft of what we need (this is what we have in our mind - not visually!)
- file with text
- Logo:
* Corporate logo
* We shelter your business logo
* ZEN & MAX series logo
- Pictograms

Specifications:
- Designed in Illustrator or InDesign
- A4 landscape (horizontal)
- 6 or 8 pages up to your design
- target audience: buyer of industrial building, purchaser, business owner

Cover:
For our other brochures we have a corporate image in which we center the use of the building. However, for the corporate brochure, we do not have an image.
We invite you to think creatively on how to create the right cover for us.

Original Illustrator files or InDesign files will be sent to us in the end together with HR print pdf.

If you have any questions - please do not hesitate to ask them!

PS: for this case we will need Translation editing done into 17 languages. Of course this will be for an additional price for you. But the winner will also get this job!

```html
<!DOCTYPE html>
<html lang="en">
<head>
<meta charset="utf-8">
<title>Kalvendor – Corporate Brochure Cover</title>
<link href="https://fonts.googleapis.com/css2?family=Josefin+Sans:wght@300&family=Montserrat:wght@300;400;700&display=swap" rel="stylesheet">
<style>
  :root {
    --backdrop: #8d8e93;
    --paper: #f4f4f4;
    --paper-edge: #e2e2e2;
    --charcoal: #2d2d2f;
    --charcoal-light: #3a3a3d;
    --rule: #8a8a8a;
    --ink: #5a5a5c;
    --white: #ffffff;
    --muted: #c9c9cb;
  }
  * { margin: 0; padding: 0; box-sizing: border-box; }
  html, body {
    width: 1200px; height: 807px; overflow: hidden;
    background: var(--backdrop);
  }
  .canvas {
    position: relative; width: 1200px; height: 807px;
    display: flex; align-items: center; justify-content: center;
  }
  .cover {
    position: relative; width: 1090px; height: 771px;
    background: var(--paper);
    box-shadow: 0 6px 24px rgba(0,0,0,.25);
    overflow: hidden;
  }
  .rule {
    position: absolute; height: 1px; background: var(--rule);
  }
  .rule--top { top: 116px; left: 0; right: 0; }
  .rule--upper-slogan { top: 588px; left: 262px; right: 0; }
  .rule--lower-slogan { top: 672px; left: 60px; right: 0; }
  .hero-photo {
    position: absolute; top: 150px; left: 300px; right: 0; height: 418px;
    background: linear-gradient(160deg, #c7d4e0 0%, #a9bccd 35%, #6b7684 62%, #2e3138 85%, #1f2126 100%);
  }
  .brand-panel {
    position: absolute; top: 176px; left: 44px; width: 262px; height: 460px;
    background: linear-gradient(180deg, var(--charcoal-light), var(--charcoal));
    color: var(--white);
    padding: 0 28px;
  }
  .brand-panel__bar {
    position: absolute; top: 56px; left: 28px; width: 200px; height: 12px;
    border-radius: 6px; background: var(--white);
  }
  .brand-name {
    position: absolute; top: 150px; left: 28px;
    font-family: "Montserrat", sans-serif; font-weight: 700;
    font-size: 30px; letter-spacing: -0.5px; color: var(--white);
  }
  .brand-tagline {
    position: absolute; top: 196px; left: 28px; width: 170px;
    font-family: "Montserrat", sans-serif; font-weight: 300;
    font-size: 10.5px; letter-spacing: 2px; line-height: 1.7;
    text-transform: uppercase; color: var(--muted);
  }
  .facts {
    position: absolute; top: 290px; left: 28px; list-style: none;
  }
  .facts__item {
    display: flex; align-items: center; gap: 12px; height: 28px;
    font-family: "Montserrat", sans-serif; font-weight: 300;
    font-size: 12px; letter-spacing: 1px; text-transform: uppercase;
    color: var(--muted);
  }
  .facts__icon { width: 16px; height: 16px; flex: none; }
  .slogan {
    position: absolute; top: 606px; left: 330px;
    font-family: "Josefin Sans", sans-serif; font-weight: 300;
    font-size: 34px; letter-spacing: 10px; color: var(--ink);
    text-transform: uppercase;
  }
</style>
</head>
<body>
<div class="canvas">
  <section class="cover">
    <div class="rule rule--top"></div>

    <div class="hero-photo" role="img" aria-label="Two roofers in orange safety gear and hard hats installing steel roof panels against a clear sky"></div>

    <div class="brand-panel">
      <div class="brand-panel__bar"></div>
      <div class="brand-name">Kalvendor</div>
      <div class="brand-tagline">Innovators in steel buildings</div>
      <ul class="facts">
        <li class="facts__item">
          <svg class="facts__icon" viewBox="0 0 16 16" fill="none" stroke="#c9c9cb" stroke-width="1.1">
            <circle cx="8" cy="8" r="6.5"/><ellipse cx="8" cy="8" rx="3" ry="6.5"/>
            <line x1="1.5" y1="8" x2="14.5" y2="8"/>
          </svg>100+ countries
        </li>
        <li class="facts__item">
          <svg class="facts__icon" viewBox="0 0 16 16" fill="none" stroke="#c9c9cb" stroke-width="1.1">
            <path d="M2.5 11.5 a5.5 5.5 0 0 1 11 0"/><line x1="1" y1="11.5" x2="15" y2="11.5"/>
            <line x1="8" y1="6" x2="8" y2="9"/>
          </svg>450+ experts
        </li>
        <li class="facts__item">
          <svg class="facts__icon" viewBox="0 0 16 16" fill="none" stroke="#c9c9cb" stroke-width="1.1">
            <rect x="3" y="2" width="10" height="12"/>
            <line x1="6" y1="5" x2="6" y2="7"/><line x1="10" y1="5" x2="10" y2="7"/>
            <rect x="6.5" y="10" width="3" height="4"/>
          </svg>450+ experts
        </li>
      </ul>
    </div>

    <div class="rule rule--upper-slogan"></div>
    <div class="slogan">We shelter your business</div>
    <div class="rule rule--lower-slogan"></div>
  </section>
</div>
</body>
</html>
```